Pebble

My company name is pebble. The logo is attached. I am the business owner.
Name Gideon Thorpe
Phone number- 5553018826
email- Gideon_thorpe@quillnet.net
Website is not live yet but it will be workwithpebble.com
the current beta link is- https://site.brvhosting.com/pebble-v3/
on the back write “ find creative pros”
Use that beta link as reference for typography and colors on card.

```html
<!DOCTYPE html>
<html lang="en">
<head>
<meta charset="utf-8">
<title>Pebble – Business Card</title>
<link rel="stylesheet" href="https://fonts.googleapis.com/css2?family=Open+Sans:wght@400;700;800&display=swap">
<style>
  :root {
    --brand-orange: #c44916;
    --brand-orange-light: #e0703f;
    --card-grey: #e7e8e9;
    --ink-light: #ebebec;
    --ink-dark: #333333;
    --page-bg: #ffffff;
  }
  * { box-sizing: border-box; margin: 0; padding: 0; }
  html, body {
    width: 1200px; height: 1200px; overflow: hidden;
    background: var(--page-bg);
    font-family: "Open Sans", Arial, sans-serif;
  }
  .canvas { position: relative; width: 1200px; height: 1200px; }

  .card { position: absolute; left: 248px; width: 703px; height: 402px; overflow: hidden; }
  .card-front { top: 162px; background: var(--brand-orange); }
  .card-back { top: 636px; background: var(--card-grey); }
  .card-back .backdrop { position: absolute; inset: 0; }

  .wordmark {
    position: absolute; color: var(--ink-light);
    font-weight: 800; line-height: 1; white-space: nowrap; text-align: center;
    letter-spacing: -1px;
  }
  .tagline {
    position: absolute; color: var(--ink-light);
    font-weight: 700; line-height: 1; white-space: nowrap; text-align: center;
    letter-spacing: 1px;
  }

  .card-front .wordmark { left: 0; width: 100%; top: 137px; font-size: 84px; }
  .card-front .tagline { left: 0; width: 100%; top: 284px; font-size: 28px; }
  .card-front .site-link {
    position: absolute; left: 0; width: 100%; top: 314px; text-align: center;
    color: var(--ink-light); font-weight: 700; font-size: 20px; letter-spacing: 12.4px;
    padding-left: 12px;
  }
  .card-front .site-underline {
    position: absolute; left: 242px; top: 345px; width: 220px; height: 2px;
    background: var(--ink-light);
  }

  .card-back .wordmark { left: 430px; width: 265px; top: 40px; font-size: 59px; }
  .card-back .tagline { left: 430px; width: 265px; top: 101px; font-size: 20px; }

  .holder-name {
    position: absolute; left: 36px; top: 67px;
    color: var(--brand-orange); font-weight: 700; font-size: 36px; letter-spacing: 1.2px;
    white-space: nowrap;
  }
  .holder-title {
    position: absolute; left: 37px; top: 106px;
    color: var(--ink-dark); font-weight: 700; font-size: 20px; letter-spacing: 1px;
  }
  .title-rule {
    position: absolute; left: 37px; top: 134px; width: 292px; height: 2px;
    background: linear-gradient(to right, var(--ink-dark) 0%, var(--ink-dark) 50%, rgba(51,51,51,0) 100%);
  }

  .contact-list { position: absolute; left: 37px; top: 173px; list-style: none; }
  .contact-item { display: flex; align-items: center; height: 34px; margin-bottom: 22.5px; }
  .contact-icon { width: 34px; height: 34px; flex: none; }
  .contact-text {
    margin-left: 17px; color: var(--ink-dark); font-size: 20px; letter-spacing: 1.8px;
    white-space: nowrap;
  }
</style>
</head>
<body>
<main class="canvas">

  <section class="card card-front" aria-label="Card front">
    <div class="wordmark">PEBBLE</div>
    <div class="tagline">Find Creative Pros</div>
    <div class="site-link">workwithpebble.com</div>
    <div class="site-underline"></div>
  </section>

  <section class="card card-back" aria-label="Card back">
    <svg class="backdrop" width="703" height="402" viewBox="0 0 703 402" aria-hidden="true">
      <defs>
        <linearGradient id="fold-shade" x1="536" y1="238" x2="560" y2="290" gradientUnits="userSpaceOnUse">
          <stop offset="0" stop-color="#7a2a0c" stop-opacity="0.55"/>
          <stop offset="1" stop-color="#c44916" stop-opacity="0"/>
        </linearGradient>
      </defs>
      <polygon points="296,0 703,0 703,402 371,402 536,238" fill="var(--brand-orange)"/>
      <polygon points="536,238 590,290 540,300 500,283" fill="url(#fold-shade)"/>
      <line x1="302" y1="0" x2="540" y2="232" stroke="var(--brand-orange-light)" stroke-width="1.2"/>
      <line x1="308" y1="0" x2="545" y2="230" stroke="var(--brand-orange-light)" stroke-width="0.8" opacity="0.7"/>
      <line x1="377" y1="402" x2="510" y2="270" stroke="var(--brand-orange-light)" stroke-width="1.2"/>
    </svg>

    <div class="holder-name">GIDEON THORPE</div>
    <div class="holder-title">BUSINESS OWNER</div>
    <div class="title-rule"></div>

    <ul class="contact-list">
      <li class="contact-item">
        <svg class="contact-icon" viewBox="0 0 34 34" aria-hidden="true">
          <circle cx="17" cy="17" r="17" fill="var(--brand-orange)"/>
          <path d="M11.5 9.5c1-.9 2.1-.8 2.7.2l1.3 2.2c.5.8.3 1.6-.4 2.2l-.8.7c.7 1.8 2 3.4 3.6 4.6l.9-.6c.8-.5 1.6-.4 2.2.3l1.7 1.9c.7.8.6 1.9-.4 2.6l-1 .7c-1 .7-2.6.6-4-.4-3.2-2.2-5.6-5.3-6.7-8.9-.5-1.6-.2-3 .6-3.8z" fill="#fff"/>
        </svg>
        <span class="contact-text">5553018826</span>
      </li>
      <li class="contact-item">
        <svg class="contact-icon" viewBox="0 0 34 34" aria-hidden="true">
          <circle cx="17" cy="17" r="17" fill="var(--brand-orange)"/>
          <rect x="8" y="11" width="18" height="12" fill="#fff"/>
          <path d="M8 11l9 7 9-7M8 23l7-6M26 23l-7-6" fill="none" stroke="var(--brand-orange)" stroke-width="1.2"/>
        </svg>
        <span class="contact-text">gideon_thorpe@quillnet.net</span>
      </li>
      <li class="contact-item">
        <svg class="contact-icon" viewBox="0 0 34 34" aria-hidden="true">
          <circle cx="17" cy="17" r="17" fill="var(--brand-orange)"/>
          <g fill="none" stroke="#fff" stroke-width="1.2">
            <circle cx="17" cy="17" r="9"/>
            <ellipse cx="17" cy="17" rx="4" ry="9"/>
            <line x1="17" y1="8" x2="17" y2="26"/>
            <line x1="8" y1="17" x2="26" y2="17"/>
            <path d="M9.5 12.5h15M9.5 21.5h15"/>
          </g>
        </svg>
        <span class="contact-text">workwithpebble.com</span>
      </li>
    </ul>

    <div class="wordmark">PEBBLE</div>
    <div class="tagline">Find Creative Pros</div>
  </section>

</main>
</body>
</html>
```